Business Card Design Project

Business and Appointment Card for Medical Practice. On back of card we would like to have: blank line for patient name, Mon-Fri each with a check box next to the day, blank line for appointment date, blank line for appointment time, with option to circle am or pm.

Target Market(s)

Professional Business Associates, as well as function as patient appointment cards (on back side of card)

Industry/Entity Type

Business

Colors

Designer to choose colors to be used in the design.

```html
<!DOCTYPE html>
<html lang="en">
<head>
<meta charset="utf-8">
<title>Alder Ridge Medical Associates – Business &amp; Appointment Card</title>
<link rel="stylesheet" href="https://fonts.googleapis.com/css2?family=Cinzel:wght@700&family=EB+Garamond:ital@1&family=Tinos:wght@700&display=swap">
<style>
  :root {
    --page-bg: #f3f3f3;
    --card-bg: #ffffff;
    --card-edge: #d9d9d9;
    --green: #0f5a25;
    --green-line: #2d6a3c;
  }
  * { box-sizing: border-box; margin: 0; padding: 0; }
  html, body { width: 816px; height: 1200px; overflow: hidden; }
  body { background: var(--page-bg); position: relative; }

  .card {
    position: absolute;
    left: 157px;
    width: 509px;
    height: 315px;
    background: var(--card-bg);
    border: 1px solid var(--card-edge);
  }
  .card--front { top: 161px; }
  .card--back  { top: 677px; }

  /* Front */
  .brand {
    position: absolute;
    left: 0; right: 0; top: 70px;
    text-align: center;
    color: var(--green);
    font-family: "Cinzel", serif;
    font-weight: 700;
  }
  .brand__mark {
    width: 96px; height: 96px;
    margin: 0 auto 14px;
    border-radius: 50%;
    background: var(--green);
  }
  .brand__name { font-size: 40px; line-height: 1; letter-spacing: 0.5px; }
  .brand__sub  { font-size: 21px; line-height: 1; margin-top: 8px; letter-spacing: 1.5px; }

  /* Back */
  .rule {
    position: absolute;
    height: 1px;
    background: var(--green-line);
    left: 27px; right: 26px;
  }
  .rule--name { top: 79px; }
  .rule--when { top: 281px; }

  .appt-lead {
    position: absolute;
    top: 86px; left: 0; right: 0;
    text-align: center;
    font-family: "EB Garamond", serif;
    font-style: italic;
    font-size: 29px;
    color: var(--green);
  }

  .weekdays {
    position: absolute;
    top: 177px; left: 0; right: 0;
    display: flex;
    justify-content: center;
    gap: 9px;
    font-family: "Tinos", serif;
    font-weight: 700;
    font-size: 18px;
    color: var(--green);
  }
  .weekday { display: flex; align-items: center; gap: 2px; }
  .checkbox {
    width: 12px; height: 12px;
    border: 1.5px solid var(--green);
    box-shadow: 2px 2px 0 var(--green);
    display: inline-block;
  }

  .field-label {
    position: absolute;
    font-family: "Tinos", serif;
    font-weight: 700;
    font-size: 12px;
    color: var(--green);
  }
  .field-label--date { left: 29px; top: 265px; }
  .field-label--time { left: 251px; top: 265px; }
  .field-label--ampm { left: 408px; top: 263px; font-size: 13px; }
</style>
</head>
<body>
  <section class="card card--front" aria-label="Business card front">
    <div class="brand">
      <div class="brand__mark"></div>
      <div class="brand__name">Alder Ridge</div>
      <div class="brand__sub">Medical Associates</div>
    </div>
  </section>

  <section class="card card--back" aria-label="Appointment card back">
    <div class="rule rule--name"></div>
    <p class="appt-lead">has an appointment on</p>
    <div class="weekdays">
      <span class="weekday">MON<i class="checkbox"></i></span>
      <span class="weekday">TUES<i class="checkbox"></i></span>
      <span class="weekday">WED<i class="checkbox"></i></span>
      <span class="weekday">THURS<i class="checkbox"></i></span>
      <span class="weekday">FRI<i class="checkbox"></i></span>
    </div>
    <span class="field-label field-label--date">Date:</span>
    <span class="field-label field-label--time">Time:</span>
    <span class="field-label field-label--ampm">AM/PM</span>
    <div class="rule rule--when"></div>
  </section>
</body>
</html>
```